PowerPoint Design Project

Powerpoint design for an online marketing agency.
PP will be used as a WhitePaper to showcase our expertise.
Our USP is that we use data for marketing so the design must reflect this with charts and graphs.
A set of images is available in our flickr account
http://www.pixelvault.example/photos/kelmora/sets/48302916574021983/with/3104827561/
We already have written real content for the PP for you to work with.
Updates

1. I have added a sample of the content a 2-page extract in a word document. The full document is around 15 pages.
2. While the finished piece is to be in PowerPoint format, it will also be used as a White Paper so the design should reflect this - i.e it should be able to be read like it was a well designed Word document not just a PP
3. The design you see in the sample 2-page document is just for illustration purposes it is not intended to influence the final design at all. So for example it currently has some pull-quotes in black boxes - that is just to show what they are and I don't want the final piece to have black boxes around quotes.
4. I've been asked to make this project guaranteed: as this is the first time I've used ArtHivePro I'm going to keep it as a standard project but we are committed to the work.
5. The current deadline is for the START of design work. We need the completed design by 21 September, so there is plenty of time to schedule this in with your other work.
Many thanks
Nigel 

The designs shown so far would not be suitable for turning into a WhitePaper. For example the bars across the top of the design create a break at the start of each page rather than emphasise the continuous nature of the document. 

Here is an example of some great design for a similar project - and we've uploaded another sample as a file

http://www.surgeloft.example/downloads/[SURGE]-what-its-like-working-

If you asked me for some ideas on the feel of the design I would say:

1. Bold - it has to look interesting - corporate world but it doesn't need to feel dull/grey
2. Exciting 
3. Precise - easy to read , not a fussy design

Target Market(s)

Business developers, sales managers, CEOs of companies with over 5 employees but without their own marketing department

Industry/Entity Type

Marketing

Requirements
Must have
• Flawless design that says "this company is smart and means business"
Nice to have
• the powerpoint should lend itself to easy file/saveas to be delivered as a PDF and for individual slides to be extracted for presentation, or use as images in blog posts etc (so for example any page number must be easy to remove).
Should not have
• no cartoons, no line drawings, nothing to obscure easy legibility

```html
<!DOCTYPE html>
<html lang="en">
<head>
<meta charset="utf-8">
<title>Why we need a new Science of Marketing?</title>
<link href="https://fonts.googleapis.com/css2?family=Lato:ital,wght@0,400;0,700;1,400;1,700&display=swap" rel="stylesheet">
<style>
  :root {
    --ink: #1f2a3a;
    --body: #2b3546;
    --accent: #1f6fb8;
    --pie: #2f7fc4;
    --pie-dark: #1d5a93;
    --quote-bg: #dbe8f6;
    --muted: #6b7380;
    --rule: #c9ced6;
    --paper: #ffffff;
  }
  * { box-sizing: border-box; margin: 0; padding: 0; }
  html, body { width: 900px; height: 1200px; overflow: hidden; background: var(--paper); }
  body { font-family: "Lato", sans-serif; color: var(--body); position: relative; }

  .page-title {
    position: absolute; left: 45px; top: 30px;
    font-size: 26px; font-weight: 700; color: var(--ink);
  }
  .title-rule {
    position: absolute; left: 45px; top: 70px; width: 520px; height: 2px; background: var(--rule);
  }
  .hero-image {
    position: absolute; left: 585px; top: 45px; width: 285px; height: 330px;
    background: radial-gradient(circle at 50% 45%, #e59a3a 0%, #b5652a 28%, #2a3f66 60%, #141d33 100%);
  }
  .intro {
    position: absolute; left: 120px; top: 92px; width: 450px;
    font-size: 19px; line-height: 24px;
  }
  .capabilities { position: absolute; left: 75px; top: 232px; width: 510px; list-style: none; }
  .capabilities li {
    position: relative; padding-left: 60px; font-size: 18px; line-height: 23px; margin-bottom: 9px;
  }
  .capabilities li::before {
    content: ""; position: absolute; left: 4px; top: 2px; width: 20px; height: 20px;
    background: var(--muted); border-radius: 4px;
  }
  .capabilities em { font-style: italic; font-weight: 700; }
  .lead-in {
    position: absolute; left: 165px; top: 535px; width: 690px;
    font-size: 17px; font-style: italic; color: var(--accent); line-height: 1.35;
  }
  .stat { position: absolute; left: 110px; width: 440px; }
  .stat svg { position: absolute; left: 0; top: 0; }
  .stat-text { position: absolute; left: 235px; top: 12px; width: 210px; font-size: 18px; line-height: 1.3; }
  .stat-source { position: absolute; left: 10px; top: 192px; font-size: 9px; color: var(--muted); }
  .stat-segment { top: 600px; height: 210px; }
  .stat-mobile { top: 845px; height: 210px; }
  .quote-box {
    position: absolute; left: 555px; top: 600px; width: 315px; height: 360px;
    background: var(--quote-bg); padding: 18px 22px;
    font-size: 17px; line-height: 1.35; color: var(--accent); font-style: italic;
  }
  .quote-mark { font-size: 44px; line-height: 0.6; font-weight: 700; color: var(--accent); vertical-align: -14px; }
  .quote-box strong { font-weight: 700; }
  .puzzle-image {
    position: absolute; left: 590px; top: 965px; width: 290px; height: 190px;
    background: linear-gradient(135deg, #4a8fdc 0%, #1f5fb0 60%, #163f7a 100%);
  }
  .copyright { position: absolute; left: 15px; top: 1168px; font-size: 13px; color: var(--body); }
</style>
</head>
<body>
  <h1 class="page-title">Why we need a new Science of Marketing?</h1>
  <div class="title-rule"></div>
  <div class="hero-image" role="img" aria-label="Glowing brain inside a human head"></div>

  <p class="intro">Traditional marketing is broken, so marketers and senior managers responsible for marketing budgets need a new game plan. Advances in technology mean our prospective clients can now:</p>

  <ul class="capabilities">
    <li>Block unwanted phone calls with caller ID, and register on official <em>do not call</em> databases</li>
    <li>Ignore sales emails with sophisticated email filtering</li>
    <li>Eliminate on-screen advertising with pop-up blockers</li>
    <li>And the level of direct mail has reached such a deluge it typically ends in the recycling bin without ever having been seen: there’s a reason why marketers call it <em>direct mail</em> when we send it, but <em>junk mail</em> when we receive it.</li>
  </ul>

  <p class="lead-in">If prospective clients can’t see or hear your current marketing and messages how can you attract leads and turn them into paying customers ?</p>

  <div class="stat stat-segment">
    <svg width="220" height="190" viewBox="0 0 220 190">
      <ellipse cx="105" cy="102" rx="98" ry="82" fill="var(--pie-dark)"/>
      <circle cx="105" cy="92" r="41" fill="none" stroke="var(--pie)" stroke-width="82"
              stroke-dasharray="216.4 257.6" transform="rotate(-90 105 92)"/>
      <path d="M105 92 L105 10 A82 82 0 0 0 30.6 57.4 Z" fill="var(--paper)" stroke="var(--rule)" stroke-width="1"/>
      <text x="115" y="140" font-family="Lato, sans-serif" font-size="26" fill="#fff">84%</text>
    </svg>
    <p class="stat-text">84% of B2B marketers segment their email campaigns</p>
    <p class="stat-source">Source: Industry Survey 2012</p>
  </div>

  <div class="stat stat-mobile">
    <svg width="220" height="190" viewBox="0 0 220 190">
      <ellipse cx="105" cy="102" rx="98" ry="82" fill="var(--pie-dark)"/>
      <circle cx="105" cy="92" r="41" fill="none" stroke="var(--pie)" stroke-width="82"
              stroke-dasharray="208.1 257.6" transform="rotate(-90 105 92)"/>
      <path d="M105 92 L105 10 A82 82 0 0 0 28.6 62.2 Z" fill="var(--paper)" stroke="var(--rule)" stroke-width="1"/>
      <text x="100" y="140" font-family="Lato, sans-serif" font-size="26" fill="#fff">80.8%</text>
    </svg>
    <p class="stat-text">Most of your leads are reading email on their mobile devices</p>
    <p class="stat-source">Source: Email Trends Report 2011</p>
  </div>

  <blockquote class="quote-box"><span class="quote-mark">“</span> <strong>Behavioral economics</strong> shows the effects of social, cognitive, and emotional factors on how humans make buying and other economic decisions. It affects the price customers are willing to pay; the timing of buying decisions; and the value customers attach to products and services. It integrates findings from behavioral and cognitive science, psychology and economics and neuroscience.</blockquote>

  <div class="puzzle-image" role="img" aria-label="Blue jigsaw puzzle pieces fitting together"></div>

  <p class="copyright">©2012 kelmora and or it’s affiliates. All Rights Reserved.</p>
</body>
</html>
```